Parkinson's Disease Progression

Visually describe the rate of Parkinson progression in the first 15 years following diagnosis. Title: "Patient-Perceived Progression of Parkinsonism"

The attached figure names "meanqol" is the curve that should serve as the basis of this graphic. Everything else-- color, labels, font, etc. describe this curve.
Thank you!

Target Market(s)

People with Parkisnon's Disease, neurologists, family members.

Font styles to use
Sans Serif

Requirements
Must have
• Must have the lines going through these exact numbers
Excellent -- 502
Very good- 661
Good- 895
Fair- 1268
Poor- 1655

LABELS:
Title: "Patient-Perceived Progression of Parkinsonism"
"SWI-TC (Self-Logged Wellbeing Index for Tremor Conditions)" should be the label on the left.
"Quality of Life" should be the label on the right
"Years Since Diagnosis" should be the label on the bottom
Nice to have
• A color scheme that goes from GOOD (low numbers) to BAD (high numbers).

Easy to read (elderly)

```html
<!DOCTYPE html>
<html lang="en">
<head>
<meta charset="UTF-8">
<title>Patient-Perceived Progression of Parkinsonism</title>
<link href="https://fonts.googleapis.com/css2?family=Lato:wght@400;700;900&display=swap" rel="stylesheet">
<style>
  :root {
    --page: #ffffff;
    --header-green: #066937;
    --panel-green: #b3d980;
    --ink-green: #066937;
    --band-poor: #d52b7d;
    --band-fair: #ad1f7e;
    --band-good: #6e1f75;
    --band-very-good: #0f6bb5;
    --band-excellent: #034390;
    --trend: #f5ee1d;
    --interval: #ffffff;
    --label: #ffffff;
  }
  html, body {
    margin: 0;
    padding: 0;
    width: 1200px;
    height: 923px;
    overflow: hidden;
    background: var(--page);
    font-family: "Lato", Arial, sans-serif;
  }
  .poster {
    position: relative;
    width: 1200px;
    height: 923px;
  }
  .title-band {
    position: absolute;
    left: 92px;
    top: 69px;
    width: 1015px;
    height: 106px;
    background: var(--header-green);
    display: flex;
    align-items: center;
    justify-content: center;
  }
  .title-band h1 {
    margin: 0;
    color: var(--label);
    font-weight: 700;
    font-size: 35px;
    letter-spacing: 0.2px;
    white-space: nowrap;
  }
  .chart {
    position: absolute;
    left: 0;
    top: 0;
    width: 1200px;
    height: 923px;
  }
  .chart text { font-family: "Lato", Arial, sans-serif; }
  .axis-number { fill: var(--ink-green); font-size: 36px; font-weight: 700; }
  .axis-title { fill: var(--ink-green); font-size: 44px; font-weight: 900; }
  .axis-subtitle { fill: var(--ink-green); font-size: 25px; font-weight: 400; }
  .band-label { fill: var(--label); font-size: 43px; font-weight: 900; }
  .tick { stroke: #1a1a1a; stroke-width: 3; }
  .trend-line { fill: none; stroke: var(--trend); stroke-width: 6; stroke-linecap: round; stroke-linejoin: round; }
  .interval-line { fill: none; stroke: var(--interval); stroke-width: 3; stroke-dasharray: 6 6; stroke-linecap: round; }
</style>
</head>
<body>
<div class="poster">
  <svg class="chart" viewBox="0 0 2000 1538" width="1200" height="923" aria-label="Line chart of SWI-TC score over 15 years since diagnosis">
    <rect class="panel" x="155" y="301" width="1692" height="1121" fill="var(--panel-green)"/>

    <!-- quality bands -->
    <rect x="508" y="380" width="1136" height="112" fill="var(--band-poor)"/>
    <rect x="508" y="492" width="1136" height="217" fill="var(--band-fair)"/>
    <rect x="508" y="709" width="1136" height="132" fill="var(--band-good)"/>
    <rect x="508" y="841" width="1136" height="96" fill="var(--band-very-good)"/>
    <rect x="508" y="937" width="1136" height="291" fill="var(--band-excellent)"/>

    <text class="band-label" x="566" y="453">POOR-1655</text>
    <text class="band-label" x="566" y="617">FAIR-1268</text>
    <text class="band-label" x="566" y="786">GOOD-895</text>
    <text class="band-label" x="856" y="908">VERY GOOD - 661</text>
    <text class="band-label" x="566" y="1124">EXCELLENT- 502</text>

    <!-- y axis -->
    <g class="y-axis">
      <line class="tick" x1="477" y1="415" x2="508" y2="415"/>
      <line class="tick" x1="477" y1="531" x2="508" y2="531"/>
      <line class="tick" x1="477" y1="647" x2="508" y2="647"/>
      <line class="tick" x1="477" y1="764" x2="508" y2="764"/>
      <line class="tick" x1="477" y1="880" x2="508" y2="880"/>
      <line class="tick" x1="477" y1="996" x2="508" y2="996"/>
      <line class="tick" x1="477" y1="1112" x2="508" y2="1112"/>
      <text class="axis-number" x="460" y="427" text-anchor="end">1600</text>
      <text class="axis-number" x="460" y="543" text-anchor="end">1200</text>
      <text class="axis-number" x="460" y="659" text-anchor="end">1000</text>
      <text class="axis-number" x="460" y="776" text-anchor="end">800</text>
      <text class="axis-number" x="460" y="892" text-anchor="end">600</text>
      <text class="axis-number" x="460" y="1008" text-anchor="end">400</text>
      <text class="axis-number" x="460" y="1124" text-anchor="end">200</text>
    </g>

    <!-- x axis -->
    <g class="x-axis">
      <line class="tick" x1="543" y1="1228" x2="543" y2="1260"/>
      <line class="tick" x1="896" y1="1228" x2="896" y2="1260"/>
      <line class="tick" x1="1248" y1="1228" x2="1248" y2="1260"/>
      <line class="tick" x1="1601" y1="1228" x2="1601" y2="1260"/>
      <text class="axis-number" x="543" y="1312" text-anchor="middle">0</text>
      <text class="axis-number" x="896" y="1312" text-anchor="middle">5</text>
      <text class="axis-number" x="1250" y="1312" text-anchor="middle">10</text>
      <text class="axis-number" x="1603" y="1312" text-anchor="middle">15</text>
    </g>

    <text class="axis-title" x="1037" y="1376" text-anchor="middle">YEARS SINCE DIAGNOSIS</text>
    <text class="axis-title" transform="translate(288 770) rotate(-90)" text-anchor="middle">SWI-TC</text>
    <text class="axis-subtitle" transform="translate(322 770) rotate(-90)" text-anchor="middle">(Self-Logged Wellbeing Index for Tremor Conditions)</text>
    <text class="axis-title" transform="translate(1742 770) rotate(-90)" text-anchor="middle">QUALITY OF LIFE</text>

    <!-- confidence interval -->
    <path class="interval-line" d="M548,914 C600,908 650,890 700,866 C760,836 820,800 880,790 C940,780 1010,784 1050,776 C1120,760 1180,720 1250,684 C1320,645 1380,620 1440,596 C1500,575 1550,550 1598,517"/>
    <path class="interval-line" d="M548,1028 C590,985 640,940 700,912 C760,880 820,845 880,828 C940,815 1020,822 1070,810 C1140,790 1190,755 1250,727 C1320,694 1390,672 1450,665 C1510,660 1560,665 1595,675"/>

    <!-- mean quality of life -->
    <path class="trend-line" d="M548,970 C620,925 680,890 740,858 C800,826 840,805 900,802 C960,799 1010,805 1060,795 C1120,780 1180,740 1250,706 C1320,672 1380,644 1450,625 C1510,610 1560,602 1598,595"/>
  </svg>

  <header class="title-band">
    <h1>PATIENT-PERCEIVED PROGRESSION OF PARKINSONISM</h1>
  </header>
</div>
</body>
</html>
```